Letterhead Design Project

I need letterhead designed for my law firm. It would also be used for web based stuff as well.

Industry/Entity Type

Law Firm

```html
<!DOCTYPE html>
<html lang="en">
<head>
<meta charset="utf-8">
<title>Hartwell &amp; Soto Law Firm – Letterhead</title>
<link rel="stylesheet" href="https://fonts.googleapis.com/css2?family=Marcellus+SC&family=Montserrat:wght@600&family=Tinos&display=swap">
<style>
  :root {
    --ink-brown: #5a4d45;
    --accent-blue: #1b8fbf;
    --body-text: #3a3a3a;
    --muted-text: #555;
    --badge-fill: #def0f8;
    --badge-shadow: #d6d6d6;
    --footer-band: #655a52;
    --footer-line: #1b9ad0;
    --footer-name: #ddd8d3;
    --footer-sub: #4a413b;
    --watermark: rgba(140, 140, 140, 0.16);
    --paper: #ffffff;
  }
  * { margin: 0; padding: 0; box-sizing: border-box; }
  html, body { width: 927px; height: 1200px; overflow: hidden; background: var(--paper); }
  .letterhead { position: relative; width: 927px; height: 1200px; background: var(--paper); overflow: hidden; }

  .firm-badge { position: absolute; left: 101px; top: 49px; width: 190px; height: 190px; border-radius: 50%;
    background: var(--badge-fill); display: flex; align-items: center; justify-content: center; text-align: center; }
  .firm-badge__name { font-family: "Tinos", serif; font-size: 22px; line-height: 1.2; color: var(--ink-brown); }
  .firm-badge__shadow { position: absolute; left: 141px; top: 236px; width: 110px; height: 12px; border-radius: 50%;
    background: radial-gradient(ellipse at center, var(--badge-shadow) 0%, rgba(214,214,214,0) 70%); }

  .masthead { position: absolute; right: 57px; top: 52px; text-align: right; }
  .masthead__name { font-family: "Marcellus SC", serif; font-size: 50px; line-height: 1; color: var(--ink-brown); letter-spacing: 1px; }
  .masthead__sub { font-family: "Montserrat", sans-serif; font-weight: 600; font-size: 25px; letter-spacing: 2px; color: var(--ink-brown); margin-top: 6px; }
  .contact { position: absolute; right: 57px; top: 158px; text-align: right; font-family: "Tinos", serif; font-size: 15px; line-height: 20.5px; color: var(--body-text); }

  .watermark { position: absolute; left: 113px; width: 710px; top: 560px; text-align: center;
    font-family: "Marcellus SC", serif; font-size: 56px; color: var(--watermark); letter-spacing: 4px; }
  .watermark__sub { display: block; font-family: "Montserrat", sans-serif; font-weight: 600; font-size: 26px; margin-top: 170px; letter-spacing: 2px; }

  .letter-body { position: absolute; left: 113px; top: 416px; width: 720px; font-family: "Tinos", serif; font-size: 17px; line-height: 23.6px; color: var(--body-text); }
  .letter-body p + p { margin-top: 23px; }
  .sign-off { position: absolute; left: 118px; top: 832px; font-family: "Tinos", serif; font-size: 17px; color: var(--muted-text); }
  .sign-off p + p { margin-top: 24px; }

  .footer-line { position: absolute; left: 0; top: 1071px; width: 927px; height: 8px; background: var(--footer-line); }
  .footer-band { position: absolute; left: 0; top: 1080px; width: 927px; height: 120px; background: var(--footer-band); }
  .footer-mark { position: absolute; right: 57px; top: 1103px; text-align: right; }
  .footer-mark__name { font-family: "Marcellus SC", serif; font-size: 36px; line-height: 1; color: var(--footer-name); letter-spacing: 1px; }
  .footer-mark__sub { font-family: "Montserrat", sans-serif; font-weight: 600; font-size: 22px; letter-spacing: 2px; color: var(--footer-sub); margin-top: 4px; }
</style>
</head>
<body>
<main class="letterhead">
  <div class="firm-badge"><span class="firm-badge__name">Hartwell &amp; Soto</span></div>
  <div class="firm-badge__shadow"></div>

  <header class="masthead">
    <div class="masthead__name">Hartwell &amp; Soto</div>
    <div class="masthead__sub">LAW FIRM</div>
  </header>
  <address class="contact" style="font-style:normal">
    P.O. Box 4180, Lakeview Ave, WA 98112<br>
    Phone : 206-555-0142<br>
    Fax: 206-555-0178<br>
    www.hartwellsoto.com
  </address>

  <div class="watermark" aria-hidden="true">Hartwell &amp; Soto<span class="watermark__sub">LAW FIRM</span></div>

  <section class="letter-body">
    <p>Lorem Ipsum is simply dummy text of the printing and typesetting industry. Lorem Ipsum has been the industry's standard dummy text ever since the 1500s, when an unknown printer took a galley of type and scrambled it to make a type specimen book. It has survived not only five centuries, but also the leap into electronic typesetting, remaining essentially unchanged. It was popularised in the 1960s with the release of Lettermark sheets containing Lorem Ipsum passages, and more recently with desktop publishing software like Pagecraft including versions of Lorem Ipsum.</p>
    <p>Lorem Ipsum is simply dummy text of the printing and typesetting industry. Lorem Ipsum has been the industry's standard dummy text ever since the 1500s, when an unknown printer took a galley of type and scrambled it to make a type specimen book. It has survived not only five centuries, but also the leap into electronic typesetting, remaining essentially unchanged. It was popularised in the 1960s with the release of Lettermark sheets containing Lorem Ipsum passages, and more recently with desktop publishing software like Pagecraft including versions of Lorem Ipsum.</p>
  </section>

  <div class="sign-off">
    <p>Best Regards</p>
    <p>Hartwell &amp; Soto</p>
  </div>

  <div class="footer-line"></div>
  <footer class="footer-band"></footer>
  <div class="footer-mark">
    <div class="footer-mark__name">Hartwell &amp; Soto</div>
    <div class="footer-mark__sub">LAW FIRM</div>
  </div>
</main>
</body>
</html>
```